Plumweave Inc. Website & Korvix Apps Landing Pages

We need a web site design for our company. We develop software and do various consultant projects for our clients. Our products focus on the mobile platform, mainly the Korvix (business, games, social, etc.). We want to communicate that our software is simple and good as candy. The web pages should be fun to look at not loosing seriousness and credibility. Web 2.0 style and 960 grid system a must. We are opened to any overall site colour scheme suggestions (look at the sites we like below).

Must haves:
- Our logo should be seen on the site and look great on it :-) (preview attached below)
- Main home page and app landing page.
- Section links/tabs on the home page (home,apps,support,blog,contact,about)
- No text in images
- Style sheet

Looks we like:
- http://x7k3lmq9pwrtzv.pixelmoorvault.net/412_Zelto_Site/final_large.jpg
- http://x7k3lmq9pwrtzv.pixelmoorvault.net/Premium_71_Illustrative_Korvix_Landing_Page/final.jpg
- http://grelmwick.com/
- http://dorniply.ca/
- http://quatzel.com/

Industry/Entity Type

Business

Requirements
Must have
• - Company logo should look great on pages.
• - Main home page and app landing page.
• - Section links/tabs on the home page (home,apps,support,blog,contact,about)
• - Web 2.0 style.
• - 960 grid system (12 col, 16 col).
• - Sliced ann optmized
• - Exported in all major formats (psd,ai,eps,png,jpeg,etc)
• - Style sheet
Should not have
• - Text in images

```html
<!DOCTYPE html>
<html lang="en">
<head>
<meta charset="utf-8">
<title>Plumweave Inc. — Home</title>
<link rel="stylesheet" href="https://fonts.googleapis.com/css2?family=Arimo:wght@400;700&family=Open+Sans:wght@400;600&display=swap">
<style>
:root{
  --topbar:#2f3033;
  --hero-dark:#141c28;
  --hero-mid:#2e3c52;
  --red:#d40f14;
  --red-dark:#b00a0e;
  --red-light:#ea2a2e;
  --panel:#f1f1f1;
  --text:#555;
  --text-dark:#333;
  --heading:#3a3a3a;
  --rule:#d0d0d0;
  --badge:#6a6a6a;
  --footer:#3a3b3e;
  --white:#fff;
}
*{box-sizing:border-box;margin:0;padding:0}
html,body{width:981px;height:1200px;overflow:hidden}
body{position:relative;background:var(--white);font-family:"Arimo",Arial,sans-serif;color:var(--text)}
.abs{position:absolute}

/* header */
.topbar{left:0;top:0;width:981px;height:67px;background:linear-gradient(#3a3b3e,var(--topbar));}
.brand{left:113px;top:18px;font-family:"Open Sans",sans-serif;font-size:29px;font-weight:600;color:var(--white);display:flex;align-items:center;gap:10px}
.brand-dot{width:12px;height:12px;border-radius:50%;background:var(--red)}
.contact{left:697px;top:20px;color:var(--white);font-weight:700;font-size:12.5px;line-height:15px}

/* hero */
.hero{left:0;top:67px;width:981px;height:357px;background:radial-gradient(ellipse at 55% 40%,var(--hero-mid),var(--hero-dark) 75%)}
.hero-title{left:111px;top:128px;font-family:"Open Sans",sans-serif;font-size:30px;font-weight:400;color:var(--white)}
.hero-rule{left:111px;top:176px;width:313px;height:1px;background:rgba(255,255,255,.35)}
.hero-text{left:111px;top:196px;width:340px;font-size:10px;line-height:14px;color:#e4e8ee}
.btn-more{left:333px;top:283px;width:102px;height:32px;background:linear-gradient(var(--red-light),var(--red-dark));border-radius:3px;box-shadow:0 2px 4px rgba(0,0,0,.5);color:var(--white);font-family:"Open Sans",sans-serif;font-size:16px;display:flex;align-items:center;justify-content:center}
.slider-dots{left:117px;top:327px;display:flex;gap:5px}
.slider-dots span{width:7px;height:7px;border-radius:50%;background:#8a909a}
.slider-dots span:first-child{background:#e8e8e8}
.device{left:644px;top:83px;width:152px;height:220px;border-radius:16px;background:linear-gradient(135deg,#3c3f45,#111214 60%,#2a2c30)}

/* nav */
.nav{left:111px;top:371px;width:750px;height:52px;background:linear-gradient(var(--red-light),var(--red) 60%,var(--red-dark));border-radius:4px 4px 0 0;display:flex;align-items:center;font-family:"Open Sans",sans-serif;font-size:14px;color:var(--white)}
.nav a{color:var(--white);text-decoration:none;height:100%;display:flex;align-items:center;justify-content:center;border-right:1px solid rgba(0,0,0,.25);box-shadow:1px 0 0 rgba(255,255,255,.15)}
.nav a:last-child{border:none;box-shadow:none}
.nav .active{font-weight:600}

/* welcome */
.welcome{left:111px;top:423px;width:750px;height:308px;background:linear-gradient(var(--panel),var(--white));box-shadow:0 3px 4px rgba(0,0,0,.12)}
.welcome-title{left:128px;top:442px;font-family:"Open Sans",sans-serif;font-size:20px;font-weight:400;color:var(--heading)}
.welcome-text{left:128px;top:476px;width:715px;font-size:10.6px;line-height:14px;color:var(--text)}
.welcome-rule{left:133px;top:529px;width:703px;height:1px;background:var(--rule)}
.feature{width:150px}
.feature-icon{width:70px;height:58px;margin-left:40px;border-radius:8px}
.feature-title{margin-top:11px;font-family:"Open Sans",sans-serif;font-size:15px;font-weight:400;color:var(--heading);white-space:nowrap}
.feature-text{margin-top:6px;font-size:9.5px;line-height:14px;color:var(--text)}

/* articles */
.thumb{left:111px;width:206px;box-shadow:0 2px 3px rgba(0,0,0,.25);border:1px solid #ddd}
.article{left:337px;width:248px}
.article-title{font-family:"Open Sans",sans-serif;font-size:15px;font-weight:400;color:var(--heading)}
.article-text{margin-top:9px;font-size:9.5px;line-height:14px;color:var(--text)}
.article-link{font-size:10.5px;color:var(--red)}

/* events */
.events{left:608px;top:760px;width:253px;height:304px;background:linear-gradient(var(--panel),#f8f8f8);box-shadow:0 3px 4px rgba(0,0,0,.12)}
.events-title{left:631px;top:774px;font-family:"Open Sans",sans-serif;font-size:16px;font-weight:400;color:var(--heading)}
.event-date{left:631px;width:52px;height:44px;background:var(--badge);color:var(--white);text-align:center;border:2px solid var(--white);box-shadow:0 0 2px rgba(0,0,0,.3)}
.event-date::after{content:"";position:absolute;left:20px;bottom:-9px;border:5px solid transparent;border-top-color:var(--badge)}
.event-day{font-family:"Open Sans",sans-serif;font-size:22px;line-height:26px;margin-top:2px}
.event-month{font-size:8px}
.event-text{left:693px;width:150px;font-size:9.5px;line-height:14px;color:var(--text)}
.event-text b{color:var(--text-dark)}

/* footer */
.footer{left:0;top:1091px;width:981px;height:109px;background:linear-gradient(var(--footer),#2c2d30)}
.footer-brand{left:111px;top:1126px;font-family:"Open Sans",sans-serif;font-size:24px;font-weight:600;color:var(--white);display:flex;align-items:center;gap:8px}
.social{left:684px;top:1113px;display:flex;gap:14px}
.social span{width:23px;height:23px;border-radius:3px}
.copyright{right:120px;top:1172px;font-size:9.5px;color:#9a9a9a}
</style>
</head>
<body>

<header class="abs topbar"></header>
<div class="abs brand">Plumweave<span class="brand-dot"></span></div>
<div class="abs contact">Call Us: 321-654-987<br>Email:info@plumweave.com</div>

<section class="abs hero"></section>
<h1 class="abs hero-title">Stylish applications</h1>
<div class="abs hero-rule"></div>
<p class="abs hero-text">It is a long established fact that a reader will be distracted by the readable content of a page when looking at its layout. The point of using Lorem Ipsum is that it has a more-or-less normal distribution of letters, as opposed to using 'Content here, content here', making it look like readable English.</p>
<a class="abs btn-more">More info</a>
<div class="abs slider-dots"><span></span><span></span><span></span><span></span></div>
<div class="abs device" role="img" aria-label="Korvix smartphone showing its home screen"></div>

<nav class="abs nav">
  <a class="active" style="width:102px">Home</a>
  <a style="width:110px">Portfolio</a>
  <a style="width:90px">Blog</a>
  <a style="width:114px">Services</a>
  <a style="width:118px">About Us</a>
  <a style="width:216px">Contact Us</a>
</nav>

<section class="abs welcome"></section>
<h2 class="abs welcome-title">Welcome to Our Site</h2>
<p class="abs welcome-text">It is a long established fact that a reader will be distracted by the readable content of a page when looking at its layout. The point of using Lorem Ipsum is that it has a more-or-less normal distribution of letters, as opposed to using 'Content here, content here', making it look like readable English.</p>
<div class="abs welcome-rule"></div>

<div class="abs feature" style="left:135px;top:553px">
  <div class="feature-icon" role="img" aria-label="Document and pen icon" style="background:linear-gradient(#e8eef6,#b6c6dc)"></div>
  <h3 class="feature-title">Business Planning</h3>
  <p class="feature-text">It is a long established fact that a reader will be distracted by the readable content of a page when looking at its layout. The point of using Lorem Ipsum.</p>
</div>
<div class="abs feature" style="left:317px;top:553px">
  <div class="feature-icon" role="img" aria-label="Card and money icon" style="background:linear-gradient(#d9eef8,#8fc3e0)"></div>
  <h3 class="feature-title">Finance Management</h3>
  <p class="feature-text">It is a long established fact that a reader will be distracted by the readable content of a page when looking at its layout. The point of using Lorem Ipsum.</p>
</div>
<div class="abs feature" style="left:501px;top:553px">
  <div class="feature-icon" role="img" aria-label="Application window icon" style="background:linear-gradient(#cfe2f7,#3d7cc8)"></div>
  <h3 class="feature-title">Reliable application</h3>
  <p class="feature-text">It is a long established fact that a reader will be distracted by the readable content of a page when looking at its layout. The point of using Lorem Ipsum.</p>
</div>
<div class="abs feature" style="left:687px;top:553px">
  <div class="feature-icon" role="img" aria-label="Chat bubble icon" style="background:radial-gradient(circle,#8fd0f5,#1b7fcf 70%,transparent 72%)"></div>
  <h3 class="feature-title">24 Hours support</h3>
  <p class="feature-text">It is a long established fact that a reader will be distracted by the readable content of a page when looking at its layout. The point of using Lorem Ipsum.</p>
</div>

<div class="abs thumb" style="top:765px;height:142px;background:linear-gradient(#ffffff,#dfe6f5)" role="img" aria-label="Rising blue bar chart with red growth arrow"></div>
<article class="abs article" style="top:762px">
  <h3 class="article-title">Market analytics</h3>
  <p class="article-text">It is a long established fact that a reader will be distracted by the readable content of a page when looking at its layout. The point of using Lorem Ipsum.content of a page when looking at its layout. The point of using Lorem Ipsum.The point of using Lorem Ipsum.The point of using Lorem Ipsum.</p>
</article>
<a class="abs article-link" style="left:337px;top:891px">Get quote/Detail info</a>

<div class="abs thumb" style="top:936px;height:128px;background:linear-gradient(#f4f4f4,#8a8d92)" role="img" aria-label="Business team meeting around a laptop"></div>
<article class="abs article" style="top:934px">
  <h3 class="article-title">Visitor trending</h3>
  <p class="article-text">It is a long established fact that a reader will be distracted by the readable content of a page when looking at its layout. The point of using Lorem Ipsum.content of a page when looking at its layout. The point of using Lorem Ipsum.The point of using Lorem Ipsum.The point of using Lorem Ipsum.</p>
</article>
<a class="abs article-link" style="left:337px;top:1056px">Get quote/Detail info</a>

<aside class="abs events"></aside>
<h3 class="abs events-title">Upcoming Events</h3>

<div class="abs event-date" style="top:801px"><div class="event-day">24</div><div class="event-month">July/10</div></div>
<p class="abs event-text" style="top:803px"><b>It is a long established</b> fact that a reader will be distracted by the readable content of a page when looking at its layout.</p>

<div class="abs event-date" style="top:881px"><div class="event-day">18</div><div class="event-month">July/10</div></div>
<p class="abs event-text" style="top:883px"><b>It is a long established</b> fact that a reader will be distracted by the readable content of a page when looking at its layout.</p>

<div class="abs event-date" style="top:961px"><div class="event-day">09</div><div class="event-month">July/10</div></div>
<p class="abs event-text" style="top:963px"><b>It is a long established</b> fact that a reader will be distracted by the readable content of a page when looking at its layout.</p>

<footer class="abs footer"></footer>
<div class="abs footer-brand">Plumweave<span class="brand-dot" style="width:10px;height:10px"></span></div>
<div class="abs social" aria-label="Social links">
  <span style="background:#3b5a9a"></span>
  <span style="background:#3fa9d9"></span>
  <span style="background:#f08a1c"></span>
  <span style="background:#1f76b0"></span>
  <span style="background:#e8e8e8"></span>
</div>
<p class="abs copyright">Copyright © 2010 Plumweave. All Rights reserved</p>

</body>
</html>
```